Website Landing Page for Brightfall Systems

Create a custom designed website landing page for our business. Looking for a professional upscale design that incorporates our logo and logo colors into the theme. I want a standard fixed frame website, not a constant scrolling format that seems to be the trend. To start with I'm looking for more of the graphic design part, maybe a concept or theme, I don't expect to see a finished project. Not interested in generic templates or layouts.

The name of our company is Brightfall Systems and I've attached our logo below. I'd like to have the web page have the same look and feel of our logo, as well as the colors. Our company, Brightfall Systems does system design, installation, and programming, of residential and commercial Audio/Video and Automation systems. We do home theaters, lighting and building automation, video conferencing systems, security camera installations, conference rooms, projectors, distributed audio systems, and similar Technology projects. This will be a professional services/informational website. We will not sell products on this website. This website will be used to advertise our company and communicate our services to prospective customers. Having a well designed, professional and clean website is one way we want to distinguish our company from the competition.

Here are some examples of what I consider a professional well designed website
http://www.qorlamstudio.com/Work/

Last year we had our tradlo store designed (with PixelMarket) and I'm really happy with the way it turned out. You can see it at www.HolvenGearDepot.com I consider this to be a great design and looking for the same level of quality with this new website. However, do not copy or use any part of this design in this new project. This tradlo store is completely separate from our other company Brightfall Systems. I only mention this tradlo store an an example of good work.

Reason: Still going through designs.

Reason: Still working on project and have not had time to review all designs and request revisions.

Reason: Sill going through designs and requesting revisions

Reason: still going through all the submissions we received.

Target Market(s)

People interested in Audio/Video, home theaters, home automation. We do sales, system design, and programming. We typically work on larger projects with both residential and commercial customers.

Industry/Entity Type

Business

Number of Pages Required

1 page

Requirements
Must have
• Great design elements. Please use a white background. I think white goes well with our logo colors.

```html
<!DOCTYPE html>
<html lang="en">
<head>
<meta charset="utf-8">
<title>Brightfall Systems — Landing Page</title>
<link rel="stylesheet" href="https://fonts.googleapis.com/css2?family=Raleway:wght@400;500;600;700&family=Montserrat:wght@600;700&display=swap">
<style>
  :root {
    --stage: #f1f2f3;
    --white: #ffffff;
    --ink: #1c1c1c;
    --nav-ink: #2a2a2a;
    --brand-blue: #1f7cc6;
    --brand-green: #57b947;
    --band-top: #5cc247;
    --band-light: #9fd33c;
    --band-deep: #4fb547;
    --arrow-green: #56b846;
    --arrow-blue: #2c7fcf;
    --hero-top: #2d5ea6;
    --hero-mid: #3a74b9;
    --hero-low: #4d7e7a;
    --offer-panel: rgba(226, 240, 210, 0.72);
    --hex-edge: #c8e9b6;
  }
  * { margin: 0; padding: 0; box-sizing: border-box; }
  html, body { width: 1200px; height: 1200px; overflow: hidden; background: var(--stage); }
  .canvas { position: relative; width: 1200px; height: 1200px; }
  .site { position: absolute; left: 0; top: 273px; width: 1200px; height: 653px; background: var(--white); overflow: hidden; font-family: "Raleway", sans-serif; }

  /* header */
  .site-header { position: absolute; left: 0; top: 0; width: 100%; height: 73px; background: var(--white); }
  .brand { position: absolute; left: 75px; top: 10px; display: flex; align-items: center; gap: 12px; }
  .brand-mark { width: 50px; height: 50px; border-radius: 50%; background: var(--brand-blue); }
  .brand-name { font-family: "Raleway", sans-serif; font-weight: 700; font-size: 16px; line-height: 17px; color: var(--brand-blue); text-transform: uppercase; letter-spacing: 0.5px; width: 110px; }
  .main-nav { position: absolute; left: 563px; top: 37px; display: flex; gap: 24px; }
  .main-nav a { font-size: 19px; color: var(--nav-ink); text-decoration: none; font-weight: 400; padding-bottom: 2px; }
  .main-nav a.is-current { border-bottom: 3px solid var(--brand-blue); }

  /* hero */
  .hero { position: absolute; left: 0; top: 73px; width: 100%; height: 259px; }
  .hero-photo { position: absolute; inset: 0; background: linear-gradient(180deg, var(--hero-top) 0%, var(--hero-mid) 62%, var(--hero-low) 100%); }
  .hero-copy { position: absolute; left: 115px; top: 78px; color: var(--white); }
  .hero-kicker { font-size: 37px; font-weight: 500; line-height: 40px; }
  .hero-title { font-family: "Montserrat", sans-serif; font-weight: 700; font-size: 56px; line-height: 60px; letter-spacing: -0.5px; }
  .hero-text { margin-top: 6px; font-family: "Montserrat", sans-serif; font-weight: 600; font-size: 10.5px; line-height: 13.5px; width: 250px; }
  .slider-arrows { position: absolute; left: 1001px; top: 15px; display: flex; gap: 3px; }
  .slider-arrow { width: 67px; height: 37px; display: flex; align-items: center; justify-content: center; }
  .slider-arrow.prev { background: var(--arrow-green); }
  .slider-arrow.next { background: var(--arrow-blue); }
  .slider-dots { position: absolute; left: 546px; top: 236px; display: flex; gap: 5px; }
  .slider-dots span { width: 15px; height: 15px; border-radius: 50%; background: var(--white); }
  .slider-dots span.is-active { background: var(--brand-green); }

  /* green band */
  .features { position: absolute; left: 0; top: 332px; width: 100%; height: 321px; background: linear-gradient(180deg, var(--band-top) 0px, var(--band-top) 13px, var(--band-light) 14px, var(--band-deep) 140px, var(--band-deep) 100%); }
  .feature-card { position: absolute; left: 87px; width: 314px; padding: 16px 0 0 28px; }
  .feature-card.offer { top: 13px; height: 140px; background: var(--offer-panel); }
  .feature-card.did { top: 167px; height: 135px; background: var(--white); }
  .feature-title { font-size: 31px; font-weight: 600; color: var(--brand-green); line-height: 32px; margin-bottom: 4px; }
  .feature-text { font-family: "Montserrat", sans-serif; font-weight: 600; font-size: 10.5px; line-height: 13.4px; color: var(--ink); }
  .feature-more { position: absolute; left: 306px; top: 62px; }
  .project-grid { position: absolute; left: 0; top: 0; width: 1200px; height: 653px; pointer-events: none; }
  .project-grid polygon { stroke: var(--hex-edge); stroke-width: 2; }
  .project-label { font-family: "Raleway", sans-serif; font-weight: 700; font-size: 15px; fill: var(--white); }
</style>
</head>
<body>
<div class="canvas">
  <div class="site">
    <header class="site-header">
      <div class="brand">
        <span class="brand-mark"></span>
        <span class="brand-name">Brightfall Systems</span>
      </div>
      <nav class="main-nav">
        <a href="#" class="is-current">Home</a>
        <a href="#">About us</a>
        <a href="#">Services</a>
        <a href="#">Works</a>
        <a href="#">Contact us</a>
      </nav>
    </header>

    <section class="hero">
      <div class="hero-photo" role="img" aria-label="City skyline with high-rise towers under a blue sky, tinted blue"></div>
      <div class="slider-arrows">
        <span class="slider-arrow prev"><svg width="16" height="18" viewBox="0 0 16 18"><path d="M11 2 L4 9 L11 16" fill="none" stroke="#fff" stroke-width="3.5"/></svg></span>
        <span class="slider-arrow next"><svg width="16" height="18" viewBox="0 0 16 18"><path d="M5 2 L12 9 L5 16" fill="none" stroke="#fff" stroke-width="3.5"/></svg></span>
      </div>
      <div class="hero-copy">
        <p class="hero-kicker">Our Unique</p>
        <h1 class="hero-title">Landing Page</h1>
        <p class="hero-text">Lorem Ipsum is simply dummy text of the printing and typesetting industry. Lorem Ipsum has been the industry's standard dummy text ever since the 1500s</p>
      </div>
      <div class="slider-dots"><span></span><span></span><span class="is-active"></span><span></span></div>
    </section>

    <section class="features">
      <article class="feature-card offer">
        <h2 class="feature-title">What we Offer</h2>
        <p class="feature-text">Lorem Ipsum is simply dummy text<br>of the printing and typesetting industry.<br>Lorem Ipsum has been the industry's<br>standard dummy text ever since the 1500s</p>
      </article>
      <article class="feature-card did">
        <h2 class="feature-title">What we Did?</h2>
        <p class="feature-text">Lorem Ipsum is simply dummy text<br>of the printing and typesetting industry.<br>Lorem Ipsum has been the industry's<br>standard dummy text ever since the 1500s</p>
        <svg class="feature-more" width="22" height="26" viewBox="0 0 22 26"><circle cx="11" cy="13" r="11" fill="#fff"/><path d="M7 5 L15 13 L7 21" fill="none" stroke="#57b947" stroke-width="4"/></svg>
      </article>
    </section>

    <svg class="project-grid" viewBox="0 0 1200 653">
      <polygon role="img" aria-label="Auditorium with rows of seating" fill="#8f9aa3" points="590,353 659.3,393 659.3,473 590,513 520.7,473 520.7,393"/>
      <polygon role="img" aria-label="Lit residence entrance with palm trees at dusk" fill="#6a6a55" points="733,353 802.3,393 802.3,473 733,513 663.7,473 663.7,393"/>
      <polygon fill="#86cf68" fill-opacity="0.85" points="876,353 945.3,393 945.3,473 876,513 806.7,473 806.7,393"/>
      <text class="project-label" x="876" y="428" text-anchor="middle">View this</text>
      <text class="project-label" x="876" y="448" text-anchor="middle">Project</text>
      <polygon role="img" aria-label="Conference room with wood wall and screen" fill="#8f6f62" points="1018,353 1087.3,393 1087.3,473 1018,513 948.7,473 948.7,393"/>
      <polygon role="img" aria-label="Home living room with red sofa and arched windows" fill="#8c7458" points="661,476 730.3,516 730.3,596 661,636 591.7,596 591.7,516"/>
      <polygon role="img" aria-label="Glass office building facade against the sky" fill="#6f9cc9" points="804,476 873.3,516 873.3,596 804,636 734.7,596 734.7,516"/>
      <polygon role="img" aria-label="City park with trees beside a pond and tower behind" fill="#7e9a5a" points="950,476 1019.3,516 1019.3,596 950,636 880.7,596 880.7,516"/>
    </svg>
  </div>
</div>
</body>
</html>
```